Young Adult novel ebook design

The book is called Label Whore: Inspired By A True StoryIt's about a wealthy male teenager who is too much into appearances, but is later humbled by a seriea of events. I need a trendy cover that resembles other top Young Adult covers, such as the examples attached. But something unique that stands out.
Target Market(s)
Teens, young adult, middle schoolers, high schoolers
Industry/Entity Type
Writer
Colors
Designer to choose colors to be used in the design.
Requirements
Must have
- Be creative and eye catching for a teenager. Leave space for the author's name. Will reveal the name to the winner.
Nice to have
- Get inspired by some of the example covers I attached.
Should not have
- No images that clearly shows a person's race. The main character image should be up for interpretation.

```html
<!DOCTYPE html>
<html lang="en">
<head>
<meta charset="UTF-8">
<title>Velvet Mirror – Book Cover</title>
<link rel="stylesheet" href="https://fonts.googleapis.com/css2?family=Josefin+Sans:wght@300;700&family=Sacramento&display=swap">
<style>
  :root {
    --page-bg: #e9e5e0;
    --ink-white: #ffffff;
    --accent-red: #ef2b2b;
    --photo-top: #c4bdb4;
    --photo-upper: #a3958a;
    --photo-mid: #6e5d5c;
    --photo-low: #3a336f;
    --photo-bottom: #2a265e;
  }
  * { margin: 0; padding: 0; box-sizing: border-box; }
  html, body {
    width: 1200px;
    height: 1200px;
    overflow: hidden;
    background: var(--page-bg);
  }
  .book-cover {
    position: absolute;
    left: 262px;
    top: 84px;
    width: 676px;
    height: 1032px;
    overflow: hidden;
    box-shadow: 0 10px 30px rgba(0,0,0,0.25);
  }
  .cover-photo {
    position: absolute;
    inset: 0;
    background:
      radial-gradient(ellipse 38% 22% at 52% 52%, rgba(205,170,150,0.55), rgba(205,170,150,0) 100%),
      linear-gradient(180deg,
        var(--photo-top) 0%,
        var(--photo-upper) 22%,
        var(--photo-mid) 45%,
        var(--photo-low) 68%,
        var(--photo-bottom) 100%);
  }
  .title-script {
    position: absolute;
    left: 0;
    right: 0;
    top: 325px;
    text-align: center;
    font-family: "Sacramento", cursive;
    font-size: 190px;
    line-height: 1;
    color: var(--ink-white);
  }
  .title-main {
    position: absolute;
    left: 0;
    right: 0;
    top: 492px;
    text-align: center;
    font-family: "Josefin Sans", sans-serif;
    font-weight: 700;
    font-size: 124px;
    line-height: 1;
    letter-spacing: 0.06em;
    padding-left: 0.06em;
    color: var(--ink-white);
  }
  .tagline {
    position: absolute;
    left: 0;
    right: 0;
    top: 624px;
    text-align: center;
    font-family: "Josefin Sans", sans-serif;
    font-size: 30px;
    letter-spacing: 0.24em;
    padding-left: 0.24em;
    color: var(--ink-white);
    white-space: nowrap;
  }
  .tagline .light { font-weight: 300; }
  .tagline .accent { font-weight: 700; color: var(--accent-red); }
  .author-name {
    position: absolute;
    left: 0;
    right: 0;
    top: 938px;
    text-align: center;
    font-family: "Josefin Sans", sans-serif;
    font-weight: 300;
    font-size: 46px;
    letter-spacing: 0.3em;
    padding-left: 0.3em;
    color: var(--ink-white);
  }
</style>
</head>
<body>
  <div class="book-cover">
    <div class="cover-photo" role="img" aria-label="Blurred photo of a young man in a navy beanie and sweater holding up a phone that hides his face, a pale building behind him"></div>

    <div class="title-script">Velvet</div>

    <div class="title-main">MIRROR</div>

    <p class="tagline"><span class="light">DRAWN FROM </span><span class="accent">REAL DAYS</span></p>

    <p class="author-name">AUTHOR NAME</p>
  </div>
</body>
</html>
```